New business card for civil engineering company - "Keystone Audit"

We need a business card designed for our new structural engineering company.

The company name is "Keystone Audit" logo files attached.

We would like the following:
* Two-sided card
* Simple design

Information to be placed on the card:
Name - Marcus Dellow
Job Title - Director / Structural Engineer
Credentials - BEng(Hons), CPEng, CMengNZ, IntPE(NZ)
Email - marcus.dellow@keystoneaudit.co.nz
mobile - 0219364058
website - www.keystoneaudit.co.nz

```html
<!DOCTYPE html>
<html lang="en">
<head>
<meta charset="utf-8">
<title>Keystone Audit – Business Card</title>
<link rel="stylesheet" href="https://fonts.googleapis.com/css2?family=Exo+2:wght@400;500&family=Montserrat:wght@400;500&display=swap">
<style>
  :root {
    --backdrop: #d1d2d4;
    --card-white: #ffffff;
    --navy: #0d3f7a;
    --ink: #3a3a3c;
    --muted: #707073;
    --accent-blue: #6b94cc;
    --mark-light: #8ec3ea;
    --back-blue: #0b4677;
    --back-deep: #083e6c;
    --back-mark: #1a6aa6;
    --back-text: #31618f;
  }
  * { box-sizing: border-box; margin: 0; padding: 0; }
  html, body { width: 1200px; height: 1200px; overflow: hidden; }
  body {
    background: var(--backdrop);
    position: relative;
    font-family: "Montserrat", sans-serif;
  }
  .card {
    position: absolute;
    top: 266px;
    width: 384px;
    height: 670px;
    overflow: hidden;
  }
  .card--front { left: 158px; background: var(--card-white); }
  .card--back {
    left: 656px;
    background: linear-gradient(160deg, var(--back-blue) 0%, var(--back-deep) 55%, var(--back-blue) 100%);
  }

  .brand-mark { position: absolute; }
  .card--front .brand-mark {
    left: 137px; top: 96px;
    width: 110px; height: 110px;
    background: var(--mark-light);
  }
  .card--back .brand-mark {
    left: 92px; top: 292px;
    width: 200px; height: 200px;
    background: var(--back-mark);
    opacity: 0.75;
  }

  .brand-name {
    position: absolute;
    left: 0; right: 0;
    text-align: center;
    font-family: "Exo 2", sans-serif;
    font-weight: 500;
    font-size: 25px;
    letter-spacing: 3px;
    color: var(--ink);
  }
  .card--front .brand-name { top: 262px; }
  .tagline {
    position: absolute;
    left: 0; right: 0;
    text-align: center;
    font-family: "Exo 2", sans-serif;
    font-size: 11.5px;
    letter-spacing: 3.2px;
    color: var(--muted);
  }
  .card--front .tagline { top: 301px; }

  .person { position: absolute; left: 31px; top: 349px; }
  .person__name {
    font-family: "Exo 2", sans-serif;
    font-weight: 500;
    font-size: 26px;
    color: var(--navy);
    line-height: 30px;
  }
  .person__title { font-size: 17px; color: var(--ink); line-height: 24px; }
  .person__credentials { font-size: 15px; color: var(--navy); line-height: 22px; }

  .divider { position: absolute; left: 31px; right: 0; top: 457px; height: 6px; }
  .divider__thick { position: absolute; left: 0; top: 0; width: 162px; height: 6px; background: var(--navy); }
  .divider__thin { position: absolute; left: 162px; right: 0; top: 4px; height: 2px; background: var(--navy); }

  .contacts { position: absolute; left: 31px; top: 476px; list-style: none; }
  .contacts li {
    display: flex; align-items: center;
    height: 26.5px;
    font-size: 17px;
    color: var(--ink);
  }
  .contacts li.contact--email { font-size: 15.5px; }
  .contacts svg { width: 18px; height: 18px; margin-right: 13px; flex: none; }

  .corner-wedge { position: absolute; left: 0; top: 0; }

  .card--back .brand-name { top: 552px; text-align: left; left: 28px; color: var(--back-text); font-size: 27px; }
  .card--back .tagline { top: 592px; text-align: left; left: 28px; color: var(--back-text); font-size: 11.5px; }
</style>
</head>
<body>
  <section class="card card--front" aria-label="Card front">
    <div class="brand-mark" aria-hidden="true"></div>
    <div class="brand-name">KEYSTONE AUDIT</div>
    <div class="tagline">PEER REVIEW SPECIALISTS</div>

    <div class="person">
      <div class="person__name">Marcus Dellow</div>
      <div class="person__title">Director / Structural Engineer</div>
      <div class="person__credentials">BEng(Hons), CPEng, CMengNZ,<br>IntPE(NZ)</div>
    </div>

    <div class="divider"><span class="divider__thick"></span><span class="divider__thin"></span></div>

    <ul class="contacts">
      <li class="contact--phone">
        <svg viewBox="0 0 18 18" aria-hidden="true"><rect x="4.5" y="1" width="9" height="16" rx="1.5" fill="none" stroke="#0d3f7a" stroke-width="2"/><circle cx="9" cy="14" r="1" fill="#0d3f7a"/></svg>
        0219 364 058
      </li>
      <li class="contact--email">
        <svg viewBox="0 0 18 18" aria-hidden="true"><rect x="1.5" y="4" width="15" height="10" fill="none" stroke="#0d3f7a" stroke-width="1.5"/><path d="M1.5 4.5 L9 10 L16.5 4.5" fill="none" stroke="#0d3f7a" stroke-width="1.5"/></svg>
        marcus.dellow@keystoneaudit.co.nz
      </li>
      <li class="contact--web">
        <svg viewBox="0 0 18 18" aria-hidden="true" fill="none" stroke="#0d3f7a" stroke-width="1.4"><circle cx="9" cy="9" r="7.5"/><ellipse cx="9" cy="9" rx="3.2" ry="7.5"/><path d="M1.5 9h15M3 5h12M3 13h12"/></svg>
        www.keystoneaudit.co.nz
      </li>
    </ul>

    <svg class="corner-wedge" width="384" height="670" viewBox="0 0 384 670" aria-hidden="true">
      <polygon points="31,670 384,542 384,670" fill="var(--accent-blue)"/>
    </svg>
  </section>

  <section class="card card--back" aria-label="Card back">
    <div class="brand-mark" aria-hidden="true"></div>
    <div class="brand-name">KEYSTONE AUDIT</div>
    <div class="tagline">PEER REVIEW SPECIALISTS</div>
  </section>
</body>
</html>
```